Chorus of the Pacific Presents

Show name:
Bloom Melody Revue
Location:
Del Paso High School
4218 Larkmoor Ln, Citrus Heights, CA 95610
Times: 2 p.m. & 7 p.m.
Special Guests:
Hold Chord
Harbor Quartet
Brightwater Five
Ticket Prices:
VIP $35.00
General $25.00
Student $15.00

```html
<!DOCTYPE html>
<html lang="en">
<head>
<meta charset="utf-8">
<title>Bloom Melody Revue – Chorus of the Pacific</title>
<link rel="stylesheet" href="https://fonts.googleapis.com/css2?family=Cinzel:wght@400;600;700&family=Oswald:wght@500;600&family=Montserrat:wght@400;600;700&display=swap">
<style>
  :root {
    --pink-soft: #f6dcec;
    --pink-mid: #eab6d6;
    --pink-deep: #e39cc9;
    --white: #ffffff;
    --violet: #5c1bab;
    --plum: #6d2670;
    --plum-text: #6a2b72;
    --magenta: #8b2f90;
    --navy: #2f3c6b;
    --ink: #2c2c2c;
    --frame: #c48aa8;
  }
  * { margin: 0; padding: 0; box-sizing: border-box; }
  html, body { width: 790px; height: 1200px; overflow: hidden; background: var(--white); }
  .flyer {
    position: relative; width: 790px; height: 1200px; overflow: hidden;
    background: linear-gradient(180deg, var(--pink-mid) 0%, var(--pink-soft) 22%, var(--white) 45%, var(--white) 68%, var(--pink-soft) 80%, var(--pink-mid) 100%);
    font-family: "Montserrat", sans-serif; text-align: center;
  }
  .sky-photo {
    position: absolute; left: 0; top: 0; width: 100%; height: 420px;
    background: radial-gradient(ellipse at 20% 10%, rgba(255,255,255,.5), transparent 45%),
                radial-gradient(ellipse at 80% 20%, rgba(255,255,255,.4), transparent 50%),
                linear-gradient(180deg, rgba(232,170,210,.7), rgba(255,255,255,0));
  }
  .audience-photo {
    position: absolute; left: 0; bottom: 0; width: 100%; height: 360px;
    background: linear-gradient(180deg, rgba(255,255,255,0), rgba(230,160,205,.55) 55%, rgba(225,150,200,.75));
  }
  .frame { position: absolute; left: 60px; top: 28px; width: 675px; height: 605px; }
  .block { position: absolute; left: 0; width: 100%; }
  .presenter { top: 92px; font-family: "Cinzel", serif; font-weight: 600; font-size: 33px; color: var(--violet); letter-spacing: 1px; }
  .presents { top: 188px; font-size: 20px; letter-spacing: 8px; color: var(--ink); font-weight: 400; }
  .title-1 { top: 228px; font-family: "Cinzel", serif; font-weight: 700; font-size: 112px; line-height: 1; color: var(--violet); }
  .title-2 { top: 346px; font-family: "Cinzel", serif; font-weight: 700; font-size: 96px; line-height: 1; color: var(--plum); }
  .title-3 { top: 470px; font-family: "Cinzel", serif; font-weight: 400; font-size: 50px; line-height: 1; letter-spacing: 6px; color: var(--ink); }
  .date { top: 664px; font-family: "Oswald", sans-serif; font-weight: 600; font-size: 60px; line-height: 1; color: var(--plum-text); display: flex; justify-content: center; align-items: center; gap: 26px; }
  .date .sep { width: 2px; height: 44px; background: var(--plum-text); }
  .venue { top: 754px; font-weight: 700; font-size: 26px; color: var(--magenta); }
  .address { top: 790px; font-size: 20px; color: var(--ink); }
  .times { top: 824px; font-weight: 700; font-size: 21px; color: var(--violet); }
  .guests-rule { position: absolute; left: 96px; width: 600px; top: 889px; height: 2px; background: var(--violet); }
  .guests-pill {
    position: absolute; left: 277px; top: 871px; width: 236px; height: 36px; border-radius: 18px;
    background: var(--violet); color: var(--white); font-weight: 700; font-size: 17px; letter-spacing: 2px; line-height: 36px;
  }
  .guests { top: 946px; display: flex; justify-content: center; align-items: center; }
  .guest { font-weight: 700; font-size: 23px; line-height: 1.02; color: var(--navy); padding: 0 28px; }
  .guest + .guest { border-left: 1.5px solid var(--navy); }
  .tickets {
    position: absolute; left: 96px; top: 1040px; width: 604px; height: 88px; display: flex;
    border-radius: 8px; overflow: hidden; background: var(--plum);
  }
  .tickets-label {
    width: 56px; background: var(--violet); color: var(--white); font-weight: 700; font-size: 16px; line-height: 1;
    writing-mode: vertical-rl; transform: rotate(180deg); display: flex; align-items: center; justify-content: center;
  }
  .tier { flex: 1; display: flex; flex-direction: column; justify-content: center; color: var(--white); font-weight: 700; font-size: 28px; line-height: 1.05; }
  .tier + .tier { border-left: 1.5px solid rgba(255,255,255,.8); margin: 10px 0; }
  .tickets-link {
    position: absolute; left: 125px; top: 1150px; width: 540px; height: 50px; background: var(--violet);
    clip-path: polygon(5% 0, 95% 0, 100% 100%, 0 100%); border-radius: 20px 20px 0 0;
    color: var(--white); font-size: 17px; line-height: 50px;
  }
  .tickets-link strong { font-weight: 700; }
</style>
</head>
<body>
<main class="flyer">
  <div class="sky-photo" role="img" aria-label="Soft pink cloudy sky"></div>
  <div class="audience-photo" role="img" aria-label="Faded pink photo of a choir on stage"></div>

  <svg class="frame" viewBox="0 0 675 605" aria-hidden="true">
    <polygon points="200,10 560,10 660,330 470,600 170,600 10,300" fill="none" stroke="var(--frame)" stroke-width="2.5" opacity=".7"/>
    <polygon points="230,40 520,30 640,300 490,570 150,560 40,310" fill="none" stroke="var(--frame)" stroke-width="2.5" opacity=".8"/>
  </svg>

  <div class="block presenter">Chorus of the Pacific</div>
  <div class="block presents">PRESENTS</div>
  <h1 class="block title-1">BLOOM</h1>
  <div class="block title-2">MELODY</div>
  <div class="block title-3">REVUE</div>

  <div class="block date"><span>SATURDAY</span><span class="sep"></span><span>APRIL 23</span><span class="sep"></span><span>2022</span></div>
  <div class="block venue">DEL PASO HIGH SCHOOL</div>
  <div class="block address">4218 Larkmoor Ln, Citrus Heights, CA 95610</div>
  <div class="block times">TIMES: 2 P.M. &amp; 7 P.M.</div>

  <div class="guests-rule"></div>
  <div class="guests-pill">SPECIAL GUESTS</div>
  <div class="block guests">
    <div class="guest">HOLD CHORD</div>
    <div class="guest">HARBOR<br>QUARTET</div>
    <div class="guest">BRIGHTWATER<br>FIVE</div>
  </div>

  <div class="tickets">
    <div class="tickets-label">TICKET<br>PRICES</div>
    <div class="tier">VIP<br>$35.00</div>
    <div class="tier">GENERAL<br>$25.00</div>
    <div class="tier">STUDENT<br>$15.00</div>
  </div>
  <div class="tickets-link">Ticket Available : <strong>WWW.CHORUSOFTHEPACIFIC.ORG</strong></div>
</main>
</body>
</html>
```